Covid 19 Exit Strategy one page brochure

I would like to design, and will need URGENT help, a brochure detailing a Covid 19 Exit Strategy plan. This brochure will need to be understood easily and the graphics inside should make it easy for people to understand without reading the entire text. This project is quite urgent and needs to be completed THIS WEEK - by Saturday may 16th at the latest. I am attaching two examples. I will provide the text.

```html
<!DOCTYPE html>
<html lang="en">
<head>
<meta charset="utf-8">
<title>Coronavirus COVID-19 – The Exit Strategy</title>
<link href="https://fonts.googleapis.com/css2?family=Exo+2:wght@600;700&family=Open+Sans:wght@400;600;700&display=swap" rel="stylesheet">
<style>
  :root {
    --ink: #1f1f2b;
    --navy: #24223f;
    --blue-deep: #2c5079;
    --red: #ef403a;
    --covid-red: #e8302f;
    --title-blue: #2d7bcf;
    --label-blue: #1e4d84;
    --cell-light: #f4f4f5;
    --cell-dark: #e3e0e2;
    --body-text: #3a3a44;
    --white: #ffffff;
    --muted: #9a9aa2;
    --icon-red: #e8453d;
    --icon-red-soft: #f06a5f;
    --icon-blue: #2a8ee0;
    --icon-blue-soft: #5aa9ea;
    --page-bg: #ffffff;
  }
  * { box-sizing: border-box; margin: 0; padding: 0; }
  html, body { width: 890px; height: 1200px; overflow: hidden; background: var(--page-bg); }
  body { font-family: "Open Sans", sans-serif; color: var(--ink); }
  .brochure { position: relative; width: 890px; height: 1200px; background: var(--white); }

  .masthead { position: absolute; top: 42px; left: 0; width: 100%; text-align: center;
    font-family: "Exo 2", sans-serif; font-weight: 700; font-size: 28px; line-height: 34px; letter-spacing: 0.3px; }
  .masthead .line-one { color: var(--ink); }
  .masthead .covid { color: var(--covid-red); }
  .masthead .line-two { color: var(--title-blue); }

  .hero { position: absolute; top: 136px; left: 0; width: 890px; height: 232px; overflow: hidden;
    background: linear-gradient(90deg, var(--blue-deep) 0%, #6c4a68 45%, #c3444a 75%, var(--red) 100%);
    border-bottom: 3px solid var(--navy); }
  .hero-title { position: absolute; left: 75px; top: 88px; font-family: "Exo 2", sans-serif; font-weight: 700;
    font-size: 40px; color: var(--white); letter-spacing: 0.4px; line-height: 1; }
  .hero-objective { position: absolute; left: 75px; top: 137px; width: 395px; font-size: 12.5px; line-height: 16px; color: var(--white); }
  .hero-objective strong { font-weight: 700; }
  .hero-visual { position: absolute; left: 545px; top: 27px; width: 250px; height: 250px; border-radius: 50%;
    background: radial-gradient(circle, #e27a78 0%, #dd6462 58%, rgba(232,90,86,0.55) 72%, rgba(240,80,70,0) 100%); }

  .strategy-tab { position: absolute; top: 368px; left: 206px; width: 479px; height: 45px; background: var(--navy);
    border-radius: 0 0 10px 10px; clip-path: polygon(0 0, 100% 0, 97% 100%, 3% 100%);
    color: var(--white); font-size: 20px; text-align: center; line-height: 42px; }

  .steps { position: absolute; top: 460px; left: 62px; width: 764px; display: grid;
    grid-template-columns: 382px 382px; grid-template-rows: 120px 120px 120px; row-gap: 21px; }
  .step { position: relative; padding: 21px 0 0 27px; }
  .step.light { background: var(--cell-light); }
  .step.dark { background: var(--cell-dark); }
  .step-heading { font-size: 11px; font-weight: 700; line-height: 14px; color: var(--label-blue); text-transform: uppercase; }
  .step-body { margin-top: 8px; width: 212px; font-size: 11px; line-height: 14px; color: var(--body-text); text-align: justify; }
  .step-icon { position: absolute; right: 30px; top: 22px; width: 66px; height: 76px; border-radius: 4px;
    background: linear-gradient(180deg, var(--icon-red-soft) 0%, var(--icon-red) 100%); }

  .mask-note { position: absolute; top: 898px; left: 95px; width: 730px; height: 112px; }
  .mask-icon { position: absolute; left: 10px; top: 6px; width: 135px; height: 100px; border-radius: 26px 26px 50px 50px;
    background: linear-gradient(180deg, var(--icon-blue-soft) 0%, var(--icon-blue) 100%); }
  .mask-text { position: absolute; left: 205px; top: 25px; width: 500px; }
  .mask-heading { font-size: 13.5px; line-height: 19px; font-weight: 400; color: var(--ink); text-transform: uppercase; }
  .mask-body { margin-top: 6px; font-size: 11px; line-height: 14px; color: var(--body-text); }

  .contact-band { position: absolute; top: 1037px; left: 0; width: 890px; height: 99px;
    background: linear-gradient(90deg, var(--blue-deep) 0%, #7a485e 50%, var(--red) 100%); display: flex; }
  .contact { flex: 1; padding: 17px 0 0 97px; color: var(--white); }
  .contact + .contact { padding-left: 107px; border-left: 1px dashed rgba(255,255,255,0.7); margin: 14px 0; padding-top: 3px; }
  .contact-title { font-size: 14.5px; font-weight: 700; line-height: 20px; }
  .contact-body { margin-top: 9px; font-size: 11px; line-height: 14px; width: 240px; }

  .logo-slot { position: absolute; top: 1161px; left: 0; width: 100%; text-align: center;
    font-size: 14px; color: var(--muted); letter-spacing: 0.3px; }
</style>
</head>
<body>
<main class="brochure">
  <header class="masthead">
    <div class="line-one">CORONAVIRUS <span class="covid">COVID-19</span></div>
    <div class="line-two">INFORMATION AND GUIDELINES</div>
  </header>

  <section class="hero">
    <h1 class="hero-title">THE EXIT STRATEGY</h1>
    <p class="hero-objective"><strong>Objective:</strong> To gradually phase out the retrictions imposed to curb the spread of the coronavirus while remaining coutious.</p>
    <div class="hero-visual" role="img" aria-label="Illustration of hands being washed with soap"></div>
  </section>

  <div class="strategy-tab">What does the strategy consist of?</div>

  <section class="steps">
    <article class="step light">
      <h2 class="step-heading">Lorem ipsum is<br>simply dummy text</h2>
      <p class="step-body">There are many variations of passages of Lorem Ipsum available, but the majority have suffered.</p>
      <div class="step-icon" role="img" aria-label="Hospital building illustration"></div>
    </article>
    <article class="step dark">
      <h2 class="step-heading">Lorem ipsum is<br>simply dummy text</h2>
      <p class="step-body">There are many variations of passages of Lorem Ipsum available, but the majority have suffered.</p>
      <div class="step-icon" role="img" aria-label="Hospital building illustration"></div>
    </article>
    <article class="step dark">
      <h2 class="step-heading">Lorem ipsum is<br>simply dummy text</h2>
      <p class="step-body">There are many variations of passages of Lorem Ipsum available, but the majority have suffered.</p>
      <div class="step-icon" role="img" aria-label="Hospital building illustration"></div>
    </article>
    <article class="step light">
      <h2 class="step-heading">Lorem ipsum is<br>simply dummy text</h2>
      <p class="step-body">There are many variations of passages of Lorem Ipsum available, but the majority have suffered.</p>
      <div class="step-icon" role="img" aria-label="Hospital building illustration"></div>
    </article>
    <article class="step light">
      <h2 class="step-heading">Lorem ipsum is<br>simply dummy text</h2>
      <p class="step-body">There are many variations of passages of Lorem Ipsum available, but the majority have suffered.</p>
      <div class="step-icon" role="img" aria-label="Hospital building illustration"></div>
    </article>
    <article class="step dark">
      <h2 class="step-heading">Lorem ipsum is<br>simply dummy text</h2>
      <p class="step-body">There are many variations of passages of Lorem Ipsum available, but the majority have suffered.</p>
      <div class="step-icon" role="img" aria-label="Hospital building illustration"></div>
    </article>
  </section>

  <section class="mask-note">
    <div class="mask-icon" role="img" aria-label="Illustration of a blue surgical face mask"></div>
    <div class="mask-text">
      <h2 class="mask-heading">Lorem ipsum is simply dummy text of the printing and typesetting industry.</h2>
      <p class="mask-body">There are many variations of passages of Lorem Ipsum available, but the majority have suffered alteration in some form, by injected humour,</p>
    </div>
  </section>

  <footer class="contact-band">
    <div class="contact">
      <h3 class="contact-title">Questions? Contact Us.</h3>
      <p class="contact-body">There are many variations of passages of Lorem Ipsum available.</p>
    </div>
    <div class="contact">
      <h3 class="contact-title">Questions? Contact Us.</h3>
      <p class="contact-body">There are many variations of passages of Lorem Ipsum available.</p>
    </div>
  </footer>

  <div class="logo-slot">LOGO HERE</div>
</main>
</body>
</html>
```